PPT Template for a company that develops software and intellectual property for use by accountants a

We are a boutique firm that develops specialised reporting applications, financial and non-financial reporting content, checklists and other intellectual property for use by business consultants and accounting firms in particular. The applications and content we are creating is strategically focussed and we are required to produce reports and presentations and our current templates are simply not sufficient.

Excel worksheets, graphs and other graphics are regularly embedded into the presentations
We have our logo in 4 colour palettes and will require the winning version to be provided in all 4 colours plus B&W. There is one single logo but the name “Harbor Ledger Pathfinders” is presented in 3 different styles for use depending on the space available etc.
Our clients will typically take our products and rebrand/co brand these (we require them to at least say that there product is “powered by Harbor Ledger Pathfinders” with the logo.
The templates you provide will be used to create marketing presentations, proposal presentations and our standard documents that clients will rebrand or cobrand under license.

A Powerpoint Document Slide Template

Cover page layout, back page, intermediate page heading, in colours and styles based on the logo, title styles, and an intermediate or chapter heading slide style. Many of our presentations contain slides with tables, diagrams, flowcharts and text, including simple lists of bullet points. As above, you will see in our style guide that we have four coloured logos – we would like one version in each. We recommend that we finalise the design using the maroon version and then this be used as the base for the other colour palettes.
Again, the cover should be bold and draw attention but remain professional.

We are looking for something that works in both 4:3 and 16:9 (or two templates please)

We like a clear professional and simple look.

Deliverable: PowerPoint template file (.potx extension) for PowerPoint 2007 with at least a “cover” layout, a “title and content” layout, and a simplified slide layout, as well as “back cover”. Please embed any fonts used.

Industry/Entity Type

Financial

```html
<!DOCTYPE html>
<html lang="en">
<head>
<meta charset="utf-8">
<title>Harbor Ledger Pathfinders – Slide Template</title>
<link rel="stylesheet" href="https://fonts.googleapis.com/css2?family=Jost:wght@400;500;600;700&family=Open+Sans:wght@400;600&display=swap">
<style>
:root{
  --red:#d71920;
  --red-mid:#b3151b;
  --maroon:#7a0c0c;
  --fold:#4a0606;
  --grey-dark:#999999;
  --grey-light:#d3d3d3;
  --text:#555555;
  --text-soft:#777777;
  --rule:#e69a9a;
  --canvas:#ffffff;
  --sheet:#f2f1f1;
  --facet-a:#dcdcdc;
  --facet-b:#f0f0f0;
}
*{margin:0;padding:0;box-sizing:border-box}
html,body{width:1200px;height:1000px;overflow:hidden;background:var(--canvas)}
body{position:relative;font-family:"Open Sans",Arial,sans-serif;color:var(--text)}
.slide{position:absolute;width:373px;height:278px;overflow:hidden;
  background:linear-gradient(135deg,var(--facet-a) 0%,var(--facet-b) 35%,#e2e2e2 60%,var(--facet-b) 100%);
  box-shadow:3px 3px 5px rgba(0,0,0,.28)}
.sheet{position:absolute;left:10px;right:16px;top:14px;bottom:0;background:var(--sheet)}
.abs{position:absolute}
.ribbon{position:absolute;background:linear-gradient(90deg,var(--red) 0%,var(--red-mid) 55%,var(--maroon) 100%);
  clip-path:polygon(0 0,100% 0,100% 100%,0 100%,16px 50%)}
.fold{position:absolute;width:10px;height:7px;background:var(--fold);clip-path:polygon(0 0,100% 0,100% 100%)}
.slide-title{position:absolute;right:18px;top:10px;height:42px;line-height:42px;
  font-family:"Jost",Arial,sans-serif;font-weight:600;font-size:15px;color:#fff}
.brand{position:absolute;display:flex;flex-direction:column;align-items:center;gap:4px}
.brand-mark{width:18px;height:18px;border-radius:50%;background:var(--red)}
.brand-name{font-family:"Jost",Arial,sans-serif;font-weight:500;font-size:6.5px;color:var(--text);white-space:nowrap}
.footer-rule{position:absolute;top:263px;height:1px;background:var(--rule)}
.footer-brand{left:146px;top:250px;width:80px;gap:2px}
.footer-brand .brand-mark{width:9px;height:9px}
.footer-brand .brand-name{font-size:4px}
.map{position:absolute;background:radial-gradient(ellipse at 45% 45%,#efd3d3 0%,#f3e4e4 50%,#f4efef 100%)}
.cover-title{font-family:"Jost",Arial,sans-serif;font-weight:700;color:#fff;text-align:right}
.bullets{position:absolute;left:22px;right:18px;top:56px;font-size:9.6px;line-height:1.22;list-style:none}
.bullets li{position:relative;padding-left:12px;margin-bottom:6px}
.bullets li::before{content:"•";position:absolute;left:0;color:var(--red)}
.bullets ul{list-style:none;margin-top:5px}
.bullets ul li{padding-left:14px;margin-left:14px;margin-bottom:4px}
.bullets ul li::before{content:"–"}
.chart-heading{position:absolute;font-family:"Jost",Arial,sans-serif;font-weight:500;color:var(--text-soft);text-align:center}
.dash-box{position:absolute;border:1px dashed #b5b5b5}
.mini-list{position:absolute;left:206px;top:60px;width:140px;list-style:none;font-size:5.6px;line-height:1.3;color:var(--text-soft)}
.mini-list li{position:relative;padding-left:9px;margin-bottom:5px}
.mini-list li::before{content:"–";position:absolute;left:0;color:var(--red)}
.data-table{position:absolute;left:52px;top:118px;width:250px;border-collapse:separate;border-spacing:1px 0;font-size:7px;text-align:center}
.data-table th{background:var(--red);color:#fff;font-weight:400;height:13px}
.data-table td{height:13px;color:#333}
.data-table tbody tr:nth-child(odd) td{background:#dedede}
.data-table tbody tr:nth-child(even) td{background:#ebebeb}
.legend{position:absolute;list-style:none;font-size:6.5px;color:var(--text)}
.legend li{display:flex;align-items:center;gap:4px;height:14px}
.legend i{display:inline-block;width:5px;height:5px}
svg text{font-family:"Open Sans",Arial,sans-serif}
</style>
</head>
<body>

<!-- Cover -->
<section class="slide" style="left:30px;top:45px">
  <div class="sheet" style="left:10px;right:10px;top:52px;bottom:8px"></div>
  <div class="brand" style="left:22px;top:10px;align-items:flex-start">
    <span class="brand-mark"></span>
    <span class="brand-name">Harbor Ledger Pathfinders</span>
  </div>
  <div class="map" role="img" aria-label="World map made of red dots of varying size" style="left:30px;top:58px;width:322px;height:168px;border-radius:40%"></div>
  <div class="ribbon" style="left:40px;top:227px;width:325px;height:42px"></div>
  <div class="fold" style="left:355px;top:269px"></div>
  <div class="abs" style="right:22px;top:231px">
    <div class="cover-title" style="font-size:12px">PRESENTATION TITLE</div>
    <div style="font-size:7.5px;color:#fff;text-align:right;text-decoration:underline;margin-top:3px">Lorem ipsum dolor sit amet</div>
  </div>
</section>

<!-- Title and content -->
<section class="slide" style="left:416px;top:45px">
  <div class="sheet"></div>
  <div class="ribbon" style="left:44px;top:10px;width:324px;height:42px"></div>
  <div class="fold" style="left:358px;top:52px"></div>
  <h2 class="slide-title">Lorem ipsum dolor sit amet</h2>
  <ul class="bullets">
    <li>Lorem ipsum dolor sit amet, consectetur adipiscing elit. Phasellus vitae egestas elit.</li>
    <li>Quisque faucibus volutpat magna, at varius ligula lacinia eget. Maecenas hendrerit mi eu lorem pretium eu porttitor libero tempor. Ut pretium purus non enim semper imperdiet.
      <ul>
        <li>Nunc tincidunt fringilla nulla, vel lobortis risus vulputate commodo.</li>
        <li>Mauris ut lacus neque. Sed vitae nunc non enim placerat iaculis id ut mauris.</li>
      </ul>
    </li>
    <li>Nam non mi velit. Lorem ipsum dolor sit amet, consectetur adipiscing elit. In sed nisi est. Vestibulum volutpat leo vitae diam tincidunt vulputate. Suspendisse vitae nisi elit, non aliquam mi. Nulla suscipit pharetra varius.</li>
    <li>Ut pretium purus non enim semper imperdiet.</li>
  </ul>
  <div class="footer-rule" style="left:20px;width:140px"></div>
  <div class="footer-rule" style="left:212px;width:140px"></div>
  <div class="brand footer-brand"><span class="brand-mark"></span><span class="brand-name">Harbor Ledger Pathfinders</span></div>
</section>

<!-- Section heading -->
<section class="slide" style="left:800px;top:45px">
  <div class="sheet" style="left:10px;right:10px;top:0;bottom:40px"></div>
  <div class="footer-rule" style="left:20px;top:47px;width:105px"></div>
  <div class="footer-rule" style="left:248px;top:47px;width:102px"></div>
  <div class="brand" style="left:136px;top:28px;width:100px"><span class="brand-mark"></span><span class="brand-name">Harbor Ledger Pathfinders</span></div>
  <div class="abs" style="left:15px;top:120px;width:347px;height:132px;background:linear-gradient(90deg,var(--red) 0%,var(--red-mid) 60%,var(--maroon) 100%)"></div>
  <div class="abs" style="left:25px;top:112px;width:36px;height:54px;background:linear-gradient(180deg,#c4c4c4,#9a9a9a);clip-path:polygon(0 0,100% 0,100% 100%,50% 80%,0 100%)"></div>
  <div class="abs" style="left:25px;top:116px;width:36px;text-align:center;font-family:'Jost',Arial,sans-serif;font-size:17px;color:#fff">01</div>
  <h2 class="abs" style="left:76px;top:147px;font-family:'Jost',Arial,sans-serif;font-weight:600;font-size:11.5px;color:#fff">LOREM IPSUM DOLOR SIT AMET</h2>
  <div class="abs" style="left:76px;top:176px;width:272px;font-size:7.8px;line-height:1.3;color:#fff">
    <p style="margin-bottom:5px">Suspendisse potenti. Integer est nunc, dignissim ac sagittis sit amet, pretium sit amet libero.</p>
    <p>Cras id nibh et ipsum ultrices pretium. Curabitur id leo tellus, a convallis justo. In turpis magna, aliquam ut consequat et, tempor ultrices mauris.</p>
  </div>
</section>

<!-- Chart slide -->
<section class="slide" style="left:30px;top:348px">
  <div class="sheet"></div>
  <div class="ribbon" style="left:44px;top:10px;width:324px;height:42px"></div>
  <div class="fold" style="left:358px;top:52px"></div>
  <h2 class="slide-title">Chart slide 1</h2>
  <div class="chart-heading" style="left:126px;top:62px;width:120px;font-size:10px">Chart title</div>
  <svg class="abs" style="left:0;top:0" width="373" height="278" viewBox="0 0 373 278" role="img" aria-label="Clustered bar chart, three series across four categories">
    <line x1="70" y1="210" x2="305" y2="210" stroke="#cfcfcf" stroke-width="1"/>
    <g font-size="6.5" fill="#666" text-anchor="middle">
      <rect x="79" y="119.7" width="12" height="90.3" fill="var(--grey-dark)"/><text x="85" y="116">4.3</text>
      <rect x="91" y="159.6" width="12" height="50.4" fill="var(--red)"/><text x="97" y="156">2.4</text>
      <rect x="103" y="168" width="12" height="42" fill="var(--grey-light)"/><text x="109" y="164">2</text>
      <rect x="139" y="157.5" width="12" height="52.5" fill="var(--grey-dark)"/><text x="145" y="154">2.5</text>
      <rect x="151" y="117.6" width="12" height="92.4" fill="var(--red)"/><text x="157" y="114">4.4</text>
      <rect x="163" y="168" width="12" height="42" fill="var(--grey-light)"/><text x="169" y="164">2</text>
      <rect x="199" y="136.5" width="12" height="73.5" fill="var(--grey-dark)"/><text x="205" y="133">3.5</text>
      <rect x="211" y="172.2" width="12" height="37.8" fill="var(--red)"/><text x="217" y="169">1.8</text>
      <rect x="223" y="147" width="12" height="63" fill="var(--grey-light)"/><text x="229" y="143">3</text>
      <rect x="259" y="115.5" width="12" height="94.5" fill="var(--grey-dark)"/><text x="265" y="112">4.5</text>
      <rect x="271" y="151.2" width="12" height="58.8" fill="var(--red)"/><text x="277" y="148">2.8</text>
      <rect x="283" y="105" width="12" height="105" fill="var(--grey-light)"/><text x="289" y="101">5</text>
      <text x="97" y="223">Category 1</text><text x="157" y="223">Category 2</text>
      <text x="217" y="223">Category 3</text><text x="277" y="223">Category 4</text>
    </g>
    <g font-size="6.5" fill="#666">
      <rect x="136" y="231" width="5" height="5" fill="var(--grey-dark)"/><text x="143" y="236">Series 1</text>
      <rect x="173" y="231" width="5" height="5" fill="var(--red)"/><text x="180" y="236">Series 2</text>
      <rect x="210" y="231" width="5" height="5" fill="var(--grey-light)"/><text x="217" y="236">Series 3</text>
    </g>
  </svg>
  <div class="footer-rule" style="left:20px;width:140px"></div>
  <div class="footer-rule" style="left:212px;width:140px"></div>
  <div class="brand footer-brand"><span class="brand-mark"></span><span class="brand-name">Harbor Ledger Pathfinders</span></div>
</section>

<!-- Several charts + text -->
<section class="slide" style="left:416px;top:348px">
  <div class="sheet"></div>
  <div class="ribbon" style="left:44px;top:10px;width:324px;height:42px"></div>
  <div class="fold" style="left:358px;top:52px"></div>
  <h2 class="slide-title">Several charts + text slide</h2>
  <div class="dash-box" style="left:20px;top:57px;width:172px;height:94px"></div>
  <div class="dash-box" style="left:20px;top:155px;width:172px;height:97px"></div>
  <div class="dash-box" style="left:198px;top:57px;width:152px;height:195px"></div>
  <svg class="abs" style="left:0;top:0" width="373" height="278" viewBox="0 0 373 278" role="img" aria-label="Line chart and horizontal bar chart, three series from 2010 to 2013">
    <g font-size="4.5" fill="#777">
      <text x="38" y="66">6</text><text x="38" y="78.5">5</text><text x="38" y="91">4</text><text x="38" y="103.5">3</text><text x="38" y="116">2</text><text x="38" y="128.5">1</text><text x="38" y="141">0</text>
      <text x="44" y="148">2010</text><text x="71" y="148">2011</text><text x="98" y="148">2012</text><text x="124" y="148">2013</text>
    </g>
    <line x1="44" y1="140" x2="132" y2="140" stroke="#ccc" stroke-width=".6"/>
    <polyline points="48,86.3 75,108.8 102,96.3 128,83.8" fill="none" stroke="var(--grey-dark)" stroke-width="1.2"/>
    <polyline points="48,110 75,85 102,117.5 128,105" fill="none" stroke="var(--red)" stroke-width="1.2"/>
    <polyline points="48,115 75,115 102,102.5 128,77.5" fill="none" stroke="var(--maroon)" stroke-width="1.2"/>
    <g font-size="4.5" fill="#777">
      <line x1="148" y1="93" x2="156" y2="93" stroke="var(--grey-dark)"/><text x="158" y="95">A</text>
      <line x1="148" y1="104" x2="156" y2="104" stroke="var(--red)"/><text x="158" y="106">B</text>
      <line x1="148" y1="115" x2="156" y2="115" stroke="var(--maroon)"/><text x="158" y="117">C</text>
    </g>
    <g font-size="4.5" fill="#777">
      <text x="24" y="173">2013</text><text x="24" y="190">2012</text><text x="24" y="207">2011</text><text x="24" y="224">2010</text>
      <text x="39" y="246">0</text><text x="57" y="246">1</text><text x="75" y="246">2</text><text x="94" y="246">3</text><text x="112" y="246">4</text><text x="130" y="246">5</text><text x="148" y="246">6</text>
    </g>
    <line x1="40" y1="162" x2="40" y2="240" stroke="#ccc" stroke-width=".6"/>
    <rect x="40" y="164" width="91.5" height="4" fill="var(--maroon)"/><rect x="40" y="168" width="51.2" height="4" fill="var(--red)"/><rect x="40" y="172" width="82.4" height="4" fill="var(--grey-dark)"/>
    <rect x="40" y="181" width="54.9" height="4" fill="var(--maroon)"/><rect x="40" y="185" width="32.9" height="4" fill="var(--red)"/><rect x="40" y="189" width="64" height="4" fill="var(--grey-dark)"/>
    <rect x="40" y="198" width="36.6" height="4" fill="var(--maroon)"/><rect x="40" y="202" width="80.5" height="4" fill="var(--red)"/><rect x="40" y="206" width="45.8" height="4" fill="var(--grey-dark)"/>
    <rect x="40" y="215" width="36.6" height="4" fill="var(--maroon)"/><rect x="40" y="219" width="43.9" height="4" fill="var(--red)"/><rect x="40" y="223" width="78.7" height="4" fill="var(--grey-dark)"/>
    <g font-size="4.5" fill="#777">
      <rect x="156" y="197" width="3" height="3" fill="var(--maroon)"/><text x="161" y="200">C</text>
      <rect x="156" y="206" width="3" height="3" fill="var(--red)"/><text x="161" y="209">B</text>
      <rect x="156" y="215" width="3" height="3" fill="var(--grey-dark)"/><text x="161" y="218">A</text>
    </g>
  </svg>
  <ul class="mini-list">
    <li>Lorem ipsum dolor sit amet, consectetur adipiscing elit. Proin in velit facilisis libero consectetur adipiscing.</li>
    <li>Aenean congue euismod erat, eu adipiscing dui gravida in.</li>
    <li>Donec vehicula tellus sit amet est aliquam ac pretium lacus aliquam.</li>
    <li>Suspendisse potenti. Integer est nunc, dignissim ac sagittis sit amet, pretium sit amet libero.</li>
    <li>Cras id nibh et ipsum ultrices pretium. Curabitur id leo tellus, a convallis justo. In turpis magna, aliquam ut consequat et, tempor ultrices mauris.</li>
  </ul>
  <div class="footer-rule" style="left:20px;width:140px"></div>
  <div class="footer-rule" style="left:212px;width:140px"></div>
  <div class="brand footer-brand"><span class="brand-mark"></span><span class="brand-name">Harbor Ledger Pathfinders</span></div>
</section>

<!-- Table slide -->
<section class="slide" style="left:800px;top:348px">
  <div class="sheet"></div>
  <div class="ribbon" style="left:44px;top:10px;width:324px;height:42px"></div>
  <div class="fold" style="left:358px;top:52px"></div>
  <h2 class="slide-title">Table slide</h2>
  <div class="chart-heading" style="left:125px;top:82px;width:120px;font-size:10px">Table Title</div>
  <table class="data-table">
    <thead><tr><th>Category A</th><th>Category B</th><th>Category C</th><th>Category D</th></tr></thead>
    <tbody>
      <tr><td>111.222</td><td>111.333</td><td>111.444</td><td>111.999</td></tr>
      <tr><td>222.333</td><td>222.444</td><td>222.333</td><td>222.333</td></tr>
      <tr><td>333.444</td><td>333.555</td><td>333.888</td><td>333.999</td></tr>
      <tr><td>444.555</td><td>444.222</td><td>444.777</td><td>444.555</td></tr>
      <tr><td>555.222</td><td>555.777</td><td>555.888</td><td>555.222</td></tr>
    </tbody>
  </table>
  <div class="footer-rule" style="left:20px;width:140px"></div>
  <div class="footer-rule" style="left:212px;width:140px"></div>
  <div class="brand footer-brand"><span class="brand-mark"></span><span class="brand-name">Harbor Ledger Pathfinders</span></div>
</section>

<!-- Donut chart slide -->
<section class="slide" style="left:30px;top:653px">
  <div class="sheet"></div>
  <div class="ribbon" style="left:44px;top:10px;width:324px;height:42px"></div>
  <div class="fold" style="left:358px;top:52px"></div>
  <h2 class="slide-title">Lorem ipsum dolor sit amet</h2>
  <div class="abs" style="left:121px;top:71px;width:120px;text-align:center;font-family:'Jost',Arial,sans-serif;font-weight:600;font-size:10px;color:#111">Graphic Title</div>
  <svg class="abs" style="left:0;top:0" width="373" height="278" viewBox="0 0 373 278" role="img" aria-label="Donut chart of quarterly shares: 59, 17, 12 and 12 percent">
    <g transform="rotate(-90 160 158)" fill="none" stroke-width="28">
      <circle cx="160" cy="158" r="44" stroke="var(--red-mid)" stroke-dasharray="163.1 113.36"/>
      <circle cx="160" cy="158" r="44" stroke="var(--maroon)" stroke-dasharray="47 229.46" stroke-dashoffset="-163.1"/>
      <circle cx="160" cy="158" r="44" stroke="var(--grey-dark)" stroke-dasharray="33.2 243.26" stroke-dashoffset="-210.1"/>
      <circle cx="160" cy="158" r="44" stroke="var(--grey-light)" stroke-dasharray="33.2 243.26" stroke-dashoffset="-243.3"/>
    </g>
    <g font-size="7" fill="#fff" text-anchor="middle">
      <text x="200" y="174">59%</text><text x="120" y="181">17%</text><text x="121" y="143">12%</text><text x="143" y="122">12%</text>
    </g>
  </svg>
  <ul class="legend" style="left:262px;top:130px">
    <li><i style="background:var(--red-mid)"></i>1st Qtr</li>
    <li><i style="background:var(--maroon)"></i>2nd Qtr</li>
    <li><i style="background:var(--grey-dark)"></i>3rd Qtr</li>
    <li><i style="background:var(--grey-light)"></i>4th Qtr</li>
  </ul>
  <div class="footer-rule" style="left:20px;width:140px"></div>
  <div class="footer-rule" style="left:212px;width:140px"></div>
  <div class="brand footer-brand"><span class="brand-mark"></span><span class="brand-name">Harbor Ledger Pathfinders</span></div>
</section>

<!-- Back cover -->
<section class="slide" style="left:416px;top:653px">
  <div class="sheet" style="left:10px;right:10px;top:52px;bottom:8px"></div>
  <div class="brand" style="left:22px;top:10px;align-items:flex-start">
    <span class="brand-mark"></span>
    <span class="brand-name">Harbor Ledger Pathfinders</span>
  </div>
  <div class="map" role="img" aria-label="World map made of red dots of varying size" style="left:16px;top:62px;width:330px;height:160px;border-radius:40%"></div>
  <div class="ribbon" style="left:40px;top:228px;width:325px;height:42px"></div>
  <div class="fold" style="left:355px;top:270px"></div>
  <div class="abs" style="right:22px;top:233px">
    <div class="cover-title" style="font-size:12px;font-weight:500">THANK YOU</div>
    <div style="font-family:'Jost',Arial,sans-serif;font-size:7.5px;color:#fff;text-align:right;margin-top:3px">FOR YOUR TIME</div>
  </div>
</section>

</body>
</html>
```